letterhead design

can you create a letterhead using the logo you created and the following:

318 W Dunhaven Elgin IL 60123
(p) 847-555-0143
(f) 847-555-0178
www.thebrantleylawgroup.com

Industry/Entity Type

Law

Requirements
Must have
• Use logo attached: must have address 318 W Dunhaven Elgin IL 60123 phone 847-555-0143 fax 847-555-0178
Should not have
• Nothing other thank logo and address/phone/website

```html
<!DOCTYPE html>
<html lang="en">
<head>
<meta charset="utf-8">
<title>Brantley Law Group Letterhead</title>
<link href="https://fonts.googleapis.com/css2?family=Manrope:wght@300&display=swap" rel="stylesheet">
<style>
  :root {
    --gold: #e3b25b;
    --gold-pale: #f5e4c8;
    --ink: #1d1d1f;
    --paper: #ffffff;
  }
  * { margin: 0; padding: 0; box-sizing: border-box; }
  html, body { width: 848px; height: 1200px; overflow: hidden; background: var(--paper); }
  .letterhead {
    position: relative;
    width: 848px;
    height: 1200px;
    background: var(--paper);
    font-family: "Manrope", sans-serif;
    font-weight: 300;
    color: var(--ink);
  }
  .brand-block {
    position: absolute;
    left: 26px;
    top: 0;
    width: 218px;
    height: 172px;
    background: var(--gold);
    display: flex;
    flex-direction: column;
    align-items: center;
    justify-content: center;
    gap: 14px;
    color: var(--paper);
  }
  .brand-block .brand-circle { width: 62px; height: 62px; }
  .brand-name {
    text-align: center;
    font-size: 19px;
    letter-spacing: 2px;
    line-height: 1.2;
    text-transform: uppercase;
  }
  .contact-list {
    position: absolute;
    left: 517px;
    top: 56px;
    list-style: none;
  }
  .contact-item {
    display: flex;
    align-items: center;
    height: 23px;
    margin-bottom: 5px;
  }
  .contact-label {
    width: 16px;
    height: 23px;
    background: var(--gold);
    color: var(--paper);
    font-size: 13px;
    display: flex;
    align-items: flex-end;
    justify-content: center;
    padding-bottom: 2px;
    margin-right: 5px;
  }
  .contact-value {
    font-size: 20px;
    letter-spacing: -0.4px;
    line-height: 1;
    white-space: nowrap;
  }
  .watermark {
    position: absolute;
    left: 0;
    top: 450px;
    width: 848px;
    display: flex;
    flex-direction: column;
    align-items: center;
    color: var(--gold-pale);
  }
  .watermark .brand-circle { width: 184px; height: 184px; }
  .watermark-name {
    margin-top: 30px;
    font-size: 46px;
    letter-spacing: 4px;
    text-transform: uppercase;
    line-height: 1.2;
    text-align: center;
  }
  .footer-band {
    position: absolute;
    left: 0;
    bottom: 2px;
    width: 848px;
    height: 31px;
    background: var(--gold);
  }
</style>
</head>
<body>
  <div class="letterhead">
    <header>
      <div class="brand-block">
        <svg class="brand-circle" viewBox="0 0 62 62" aria-hidden="true">
          <circle cx="31" cy="31" r="29.5" fill="none" stroke="currentColor" stroke-width="1.5"/>
        </svg>
        <div class="brand-name">Brantley Law<br>Group</div>
      </div>

      <ul class="contact-list">
        <li class="contact-item"><span class="contact-label">a</span><span class="contact-value">318 W Dunhaven Elgin IL 60123</span></li>
        <li class="contact-item"><span class="contact-label">p</span><span class="contact-value">847-555-0143</span></li>
        <li class="contact-item"><span class="contact-label">f</span><span class="contact-value">847-555-0178</span></li>
        <li class="contact-item"><span class="contact-label">w</span><span class="contact-value">www.thebrantleylawgroup.com</span></li>
      </ul>
    </header>

    <div class="watermark" aria-hidden="true">
      <svg class="brand-circle" viewBox="0 0 184 184">
        <circle cx="92" cy="92" r="89" fill="none" stroke="currentColor" stroke-width="4"/>
      </svg>
      <div class="watermark-name">Brantley Law<br>Group</div>
    </div>

    <footer class="footer-band"></footer>
  </div>
</body>
</html>
```